Kovo Pays Less! Innovative Team Buying Web App

Kovo is a team-buying/social commerce web app that is a cross between Dealvark and sites/apps like Zibo, Mervane, and Lokashwin. It is basically like a game in which users seek to get the lowest prices by working with friends and neighbours (as a team) to maximize order volumes. Sellers on the platform set volume targets which teams have to hit to secure wholesale price.
We need a landing page and a few (4 - 5) key pages that project a compelling game-like aesthetic that is innovative and playful, while being clean and classy.

Target Market(s)

Nigerian homemakers. Typically 30+ years old. Predominantly female, middle class.

Industry/Entity Type

Ecommerce, Groceries.

Coding

Coded - Design and coding required

Number of Pages Required

5+ page

Requirements
Must have
• PAGES (1). Landing page. An attractive landing page that gives a brief overview of the concept and main features. We are going to roll out an MVP with just the landing page (which should include a sign-up form) so this page is critical and should be "self-contained" with it's signup inputs. The signup section must include a referral code so that we can track who referred whom. (2). Available deals. A listing of all active deals with enough relevant information. Note that deals have a deadline, a retail price, and a minimum volume target to unlock wholesale price. (3). Deal details page. This should show the standard price (the price the user would pay if he buys a small quantity), team price (the wholesale price based on the team hitting the required order volume), the points to be earned by buying the item, etc. (4). Checkout page. In addition to normal checkout stuff on this page the user can convert points into currency (at an exchange rate that may vary from time to time). Example: if price is $3,000 he may see that he has 1000 points in his wallet and the exchange rate is 1:1, so he can go ahead and convert to $1,000 and the price now becomes $2,000. (5). Profile page. Where the user can see things like his performance (how his points were calculated), his lineage ("children" and "grandchildren"), points required to get to the next rank, his order history, etc.
Nice to have
• GUIDELINES (1). Overall Aesthetic is game-like: playful, bright, and colourful. But clean and classic at the same time: we don't want a look that goes "out of fashion" within the next two or three years. (2). Referral is critical. Therefore the "Share" button (or whatever) should be easily accessible and visible on all relevant pages. (3). The user's community is critical. Therefore the activity of the users "network" (the "children" and "grandchildren") must be somehow dynamically visible at most/all times. We want to project a sense of realtime dynamism, just like a game. The user should be able to somehow "see" things happening in the network (e.g. when someone in his network buys something). (4). Like a game, the user's points, rank, and badges must always/usually be visible and we need an interesting visual effect when something happens that increases his points. Examples of actions that generate points include buying an item, when a "child" or "grandchild" buys an item, when someone you invited/referred creates an account, etc. We need a clear idea of the visual effect and how it would work.

```html
<!DOCTYPE html>
<html lang="en">
<head>
<meta charset="utf-8">
<title>Kovo — The Power of Kovo</title>
<link href="https://fonts.googleapis.com/css2?family=League+Spartan:wght@600;700&family=Mulish:wght@300;400;600;700&display=swap" rel="stylesheet">
<style>
  :root{
    --ink:#111418;
    --text:#3a3d42;
    --red:#e00d0d;
    --teal-dark:#0b3a42;
    --grey-band:#f6f4f4;
    --footer:#262626;
    --magenta:#cf4ff0;
    --orange:#e8721c;
    --navy:#3a4a85;
    --member:#d9dcea;
    --line-grey:#7a7f8a;
    --field-border:#b9bcc2;
  }
  *{box-sizing:border-box;margin:0;padding:0}
  html,body{width:1200px;height:3155px;overflow:hidden;background:#fff}
  body{font-family:"Mulish",Arial,sans-serif;color:var(--text)}
  .page{position:relative;width:1200px;height:3155px;overflow:hidden}
  .abs{position:absolute}
  .heading{font-family:"League Spartan","Mulish",sans-serif;font-weight:700;color:var(--ink);letter-spacing:.2px}
  .rule{position:absolute;height:3px;width:50px;background:var(--teal-dark)}
  .btn{position:absolute;display:flex;align-items:center;justify-content:center;background:var(--red);color:#fff;border-radius:20px;font-weight:600}

  .logo{position:absolute;font-family:"League Spartan",sans-serif;font-weight:700;font-size:26px;color:var(--ink);letter-spacing:.5px}
  .nav{position:absolute;top:34px;left:416px;font-size:14.5px;color:#222}
  .nav a{color:inherit;text-decoration:none;position:absolute;white-space:nowrap}

  .hero-art{left:132px;top:122px;width:584px;height:417px;border-radius:8px;background:linear-gradient(135deg,#f3e9f7 0%,#efe2e4 55%,#e9ecf6 100%)}
  .hero-title{left:797px;top:157px;font-size:41px;line-height:49px}
  .hero-copy{left:798px;top:268px;width:275px;font-size:16px;line-height:24px;font-weight:300;color:#333}

  .rewards-title{left:132px;top:766px;font-size:29px}
  .rewards-copy{left:132px;top:840px;width:300px;font-size:16px;line-height:22.4px;font-weight:400;color:#3a3d42}
  .member{position:absolute;width:66px;height:66px;border-radius:50%;background:var(--member)}

  .reg-title{left:0;width:1200px;top:1202px;text-align:center;font-size:29px}
  .card{left:242px;top:1304px;width:712px;height:358px;background:#fff;border-radius:22px;box-shadow:0 6px 40px rgba(0,0,0,.07)}
  .field{position:absolute;height:47px;border:1px solid var(--field-border);border-radius:24px;padding-left:23px;display:flex;align-items:center;font-size:14.5px;color:#555;background:#fff}

  .about-title{left:135px;top:1882px;font-size:29px;color:#fff}
  .about-copy{left:135px;top:1952px;width:292px;font-size:16.5px;line-height:22.4px;color:#e9eef0;font-weight:300}
  .about-art{left:484px;top:1910px;width:587px;height:365px;border-radius:300px 300px 0 0;background:radial-gradient(circle at 50% 70%,#e4f3f8 0%,#cfe7f0 45%,#2f7fa8 100%)}

  .feat-title{left:0;width:1200px;top:2324px;text-align:center;font-size:29px}
  .feat-icon{position:absolute;width:80px;height:80px;border:2.5px solid var(--teal-dark);border-radius:50%;display:flex;align-items:center;justify-content:center}
  .feat-name{position:absolute;font-weight:700;font-size:18px;color:#1b1d20}
  .feat-copy{position:absolute;font-size:15px;line-height:21.5px;font-weight:300;color:#333}

  .foot-logo{left:135px;top:2940px;color:#fff;font-size:25px}
  .foot-col{position:absolute;top:2922px;color:#d8d8d8;font-size:12.5px;line-height:19.2px}
  .foot-col h4{color:#fff;font-size:12.5px;font-weight:700;margin-bottom:4px;letter-spacing:.3px}
  .social{position:absolute;top:2951px;width:24px;height:24px;background:#fff;border-radius:2px}
  .divider{left:130px;top:3069px;width:940px;height:1px;background:#4a4a4a}
  .copyright{left:0;width:1200px;top:3104px;text-align:center;color:#e6e6e6;font-size:12px}
</style>
</head>
<body>
<div class="page">

  <div class="logo" style="left:132px;top:30px">KOVO</div>
  <nav class="nav">
    <a style="left:0">Group Buying</a>
    <a style="left:123px">Group Donations</a>
    <a style="left:268px">Group Alarm</a>
    <a style="left:386px">Group Chat</a>
    <a style="left:498px">Visitors</a>
  </nav>
  <div class="btn" style="left:994px;top:28px;width:74px;height:31px;font-size:14.5px">Login</div>

  <div class="abs hero-art" role="img" aria-label="Illustration of a woman relaxing in an armchair with a laptop, surrounded by price tags, gift boxes, a card and a magnifier"></div>
  <h1 class="abs heading hero-title">The Power<br>of Kovo</h1>
  <p class="abs hero-copy">Kovo amplifies your buying power and social impact by helping you join forces with your neighbours. Secure huge discounts, organise neighbourhood security, coordinate donations, and much more.</p>
  <div class="btn" style="left:797px;top:437px;width:85px;height:36px;font-size:14.5px">Demo</div>

  <svg class="abs" style="left:0;top:615px" width="1200" height="530" viewBox="0 0 1200 530">
    <path d="M0 90 C250 105 420 70 600 30 C800 -10 1000 -5 1200 10 L1200 530 L0 530 Z" fill="var(--grey-band)"/>
    <path d="M0 40 C50 40 90 60 107 90 L0 90 Z" fill="var(--magenta)"/>
    <path d="M1030 20 C1090 8 1150 5 1200 12 L1200 55 C1150 40 1090 28 1030 20 Z" fill="var(--magenta)"/>
  </svg>
  <h2 class="abs heading rewards-title">YOUR REWARDS</h2>
  <div class="rule" style="left:132px;top:810px"></div>
  <p class="abs rewards-copy">Don't just buy stuff on Kovo. Actively become part of the community by getting your friends and neighbours involved. You get rewarded with points which can be used not only for discounts but also as credits to partake in community activities. Kovo's referral marketing scheme allows you to generate points not only from the activity of your friends, but even friends of friends...and so on!</p>

  <svg class="abs" style="left:0;top:0" width="1200" height="1142" viewBox="0 0 1200 1142">
    <g fill="none" stroke="var(--line-grey)" stroke-width="1.3">
      <path d="M722 823 H600 V853"/>
      <path d="M818 823 H938 V853"/>
    </g>
    <g fill="var(--line-grey)"><circle cx="722" cy="823" r="2.5"/><circle cx="818" cy="823" r="2.5"/><circle cx="600" cy="853" r="2.5"/><circle cx="938" cy="853" r="2.5"/></g>
    <g fill="none" stroke="var(--orange)" stroke-width="1.3">
      <path d="M551 921 H502 V992"/>
      <path d="M647 921 H697 V992"/>
      <path d="M889 921 H841 V992"/>
      <path d="M985 921 H1036 V992"/>
    </g>
    <g fill="var(--orange)"><circle cx="551" cy="921" r="2.5"/><circle cx="647" cy="921" r="2.5"/><circle cx="889" cy="921" r="2.5"/><circle cx="985" cy="921" r="2.5"/><circle cx="502" cy="992" r="2.5"/><circle cx="697" cy="992" r="2.5"/><circle cx="841" cy="992" r="2.5"/><circle cx="1036" cy="992" r="2.5"/></g>
  </svg>
  <div class="member" role="img" aria-label="Member avatar" style="left:737px;top:778px"></div>
  <div class="member" role="img" aria-label="Referred member avatar" style="left:567px;top:874px"></div>
  <div class="member" role="img" aria-label="Referred member avatar" style="left:905px;top:874px"></div>
  <div class="member" role="img" aria-label="Second-level member avatar" style="left:467px;top:1014px"></div>
  <div class="member" role="img" aria-label="Second-level member avatar" style="left:662px;top:1014px"></div>
  <div class="member" role="img" aria-label="Second-level member avatar" style="left:808px;top:1014px"></div>
  <div class="member" role="img" aria-label="Second-level member avatar" style="left:1005px;top:1014px"></div>

  <h2 class="abs heading reg-title">REGISTER ON KOVO</h2>
  <div class="rule" style="left:575px;top:1257px"></div>
  <svg class="abs" style="left:190px;top:1255px" width="200" height="200" viewBox="0 0 200 200">
    <g fill="none" stroke="#dcdcdc" stroke-width="1.5"><circle cx="101" cy="98" r="86"/><circle cx="101" cy="98" r="74"/><circle cx="101" cy="98" r="60"/></g>
  </svg>
  <svg class="abs" style="left:860px;top:1558px" width="142" height="142" viewBox="0 0 142 142">
    <g fill="none" stroke="#dcdcdc" stroke-width="1.5"><circle cx="71" cy="71" r="59"/><circle cx="71" cy="71" r="50"/><circle cx="71" cy="71" r="40"/></g>
  </svg>
  <div class="abs card"></div>
  <div class="field" style="left:284px;top:1354px;width:305px">Phone #</div>
  <div class="field" style="left:605px;top:1354px;width:305px">Email Address</div>
  <div class="field" style="left:284px;top:1420px;width:305px">Password</div>
  <div class="field" style="left:605px;top:1420px;width:305px">Confirm Password</div>
  <div class="field" style="left:284px;top:1490px;width:626px">Referral code</div>
  <div class="btn" style="left:523px;top:1569px;width:154px;height:48px;border-radius:24px;font-size:19px;font-weight:700">SIGNUP</div>

  <svg class="abs" style="left:0;top:1740px" width="1200" height="536" viewBox="0 0 1200 536">
    <path d="M0 72 C200 95 420 70 600 30 C780 -5 1000 0 1200 25 L1200 536 L0 536 Z" fill="var(--teal-dark)"/>
  </svg>
  <h2 class="abs heading about-title">ABOUT KOVO</h2>
  <div class="rule" style="left:135px;top:1924px;width:60px;background:#fff"></div>
  <p class="abs about-copy">We believe that human beings can achieve great things through teamwork and the power of community, and we believe that this process should be enjoyable. Through our Team Buying platform, we help friends and neighbours solve economic challenges in a localised and fun way.</p>
  <div class="btn" style="left:132px;top:2178px;width:109px;height:35px;font-size:15px">Read More</div>
  <div class="abs about-art" role="img" aria-label="Illustration of three friends standing together with a laptop and communication icons around them"></div>

  <h2 class="abs heading feat-title">FEATURES</h2>
  <div class="rule" style="left:584px;top:2376px;width:40px"></div>

  <div class="feat-icon" style="left:133px;top:2441px">
    <svg width="40" height="40" viewBox="0 0 40 40" fill="none" stroke="var(--teal-dark)" stroke-width="2.5"><circle cx="13" cy="12" r="4"/><circle cx="27" cy="12" r="4"/><path d="M6 28c0-5 3-9 7-9s7 4 7 9M20 28c0-5 3-9 7-9s7 4 7 9"/><path d="M10 34h20"/></svg>
  </div>
  <div class="feat-name" style="left:246px;top:2436px">Group Buying</div>
  <p class="feat-copy" style="left:247px;top:2472px;width:245px">Want to buy at manufacturer or wholesale prices? Team up with friends and neighbours to create high volume orders.</p>

  <div class="feat-icon" style="left:659px;top:2441px">
    <svg width="40" height="40" viewBox="0 0 40 40" fill="none" stroke="var(--teal-dark)" stroke-width="2.5"><rect x="7" y="11" width="26" height="22" rx="2"/><rect x="12" y="17" width="16" height="9"/><path d="M15 6a7 7 0 0 1 10 0"/></svg>
  </div>
  <div class="feat-name" style="left:763px;top:2436px">Visitor Access Control</div>
  <p class="feat-copy" style="left:764px;top:2472px;width:275px">Generate entry or access codes for guests. Have your security personnel set up with the Kovo SP App and you're all set.</p>

  <div class="feat-icon" style="left:135px;top:2618px">
    <svg width="40" height="40" viewBox="0 0 40 40" fill="none" stroke="var(--teal-dark)" stroke-width="2.5" stroke-linejoin="round"><path d="M10 28V18a10 10 0 0 1 20 0v10l3 3H7z"/><path d="M17 35h6"/><path d="M20 6v2"/></svg>
  </div>
  <div class="feat-name" style="left:249px;top:2610px">Group Panic Alarm</div>
  <p class="feat-copy" style="left:249px;top:2646px;width:278px">Setup your friends or our professional service providers as emergency contacts and they get notified once you hit the Big Red Panic button.</p>

  <div class="feat-icon" style="left:661px;top:2618px">
    <svg width="40" height="40" viewBox="0 0 40 40" fill="none" stroke="var(--teal-dark)" stroke-width="2.5" stroke-linejoin="round"><path d="M7 18l13-6 13 6v14H7z"/><path d="M20 29s-6-3.5-6-7a3 3 0 0 1 6-1 3 3 0 0 1 6 1c0 3.5-6 7-6 7z"/></svg>
  </div>
  <div class="feat-name" style="left:766px;top:2610px">Group Donations</div>
  <p class="feat-copy" style="left:766px;top:2646px;width:282px">Fixing the soccer pitch? Donating to a local charity? Collect and disburse funds on behalf of the group quickly, securely, and transparently.</p>

  <svg class="abs" style="left:0;top:2780px" width="1200" height="375" viewBox="0 0 1200 375">
    <path d="M0 73 C200 95 360 75 520 40 C700 0 950 0 1200 8 L1200 375 L0 375 Z" fill="var(--footer)"/>
  </svg>
  <div class="abs heading foot-logo">KOVO</div>
  <div class="foot-col" style="left:301px"><h4>RESOURCES</h4>Product support<br>Request a demo<br>Online Demos (Video)</div>
  <div class="foot-col" style="left:564px"><h4>COMPANY</h4>Contact us<br>Legal</div>
  <div class="foot-col" style="left:743px"><h4>MENU</h4>Group Buying<br>Group Donations<br>Group Alarm<br>Group Chat<br>Visitors</div>
  <div class="foot-col" style="left:932px"><h4>FOLLOW US</h4></div>
  <div class="social" style="left:934px"></div>
  <div class="social" style="left:971px"></div>
  <div class="social" style="left:1007px"></div>
  <div class="social" style="left:1044px"></div>
  <div class="abs divider"></div>
  <div class="abs copyright">Copyright © 2023 All Rights Reserved</div>

</div>
</body>
</html>
```